Real Estate Agent needs business card design

We have logo designed already, want to have business card designed. Very interested in those smaller size business card as they look very trendy. Business name is called VORENDA REALTY

```html
<!DOCTYPE html>
<html lang="en">
<head>
<meta charset="utf-8">
<title>Vorenda Realty – Business Cards</title>
<link href="https://fonts.googleapis.com/css2?family=Cormorant+Garamond:wght@600;700&family=Open+Sans:wght@400;600&display=swap" rel="stylesheet">
<style>
  :root {
    --backdrop: #111111;
    --gold: #cfa46f;
    --gold-light: #d8b380;
    --gold-deep: #c49a63;
    --gold-text: #c9a06a;
    --paper: #ffffff;
    --ink: #1c1c1c;
    --ink-soft: #2a2a2a;
  }
  * { margin: 0; padding: 0; box-sizing: border-box; }
  html, body {
    width: 1200px;
    height: 1000px;
    overflow: hidden;
    background: var(--backdrop);
  }
  .stage {
    position: relative;
    width: 1200px;
    height: 1000px;
    display: flex;
    align-items: center;
    justify-content: center;
    gap: 70px;
  }
  .card {
    position: relative;
    width: 500px;
    height: 300px;
    border-radius: 26px;
    overflow: hidden;
    box-shadow: 0 18px 40px rgba(0, 0, 0, 0.55);
  }

  /* Front */
  .card-front {
    background: linear-gradient(135deg, var(--gold-light) 0%, var(--gold) 50%, var(--gold-deep) 100%);
    display: flex;
    align-items: center;
    justify-content: center;
  }
  .brand-front {
    font-family: "Cormorant Garamond", Georgia, serif;
    font-weight: 700;
    font-size: 34px;
    letter-spacing: 2px;
    color: var(--paper);
  }

  /* Back */
  .card-back {
    background: var(--paper);
    font-family: "Open Sans", Arial, sans-serif;
    color: var(--ink);
  }
  .agent {
    position: absolute;
    left: 40px;
    top: 42px;
  }
  .agent-name {
    font-family: "Cormorant Garamond", Georgia, serif;
    font-weight: 700;
    font-size: 27px;
    color: var(--gold-text);
    line-height: 1;
  }
  .agent-role {
    font-size: 14px;
    margin-top: 5px;
    color: var(--ink);
  }
  .contact {
    position: absolute;
    left: 40px;
    top: 150px;
    font-size: 15px;
    line-height: 1.45;
  }
  .brand-back {
    position: absolute;
    right: 40px;
    top: 92px;
    font-family: "Cormorant Garamond", Georgia, serif;
    font-weight: 700;
    font-size: 30px;
    letter-spacing: 1.5px;
    color: var(--ink-soft);
  }
  .address {
    position: absolute;
    right: 40px;
    bottom: 36px;
    font-size: 16px;
    line-height: 1.35;
    text-align: left;
  }
</style>
</head>
<body>
  <main class="stage">
    <section class="card card-front" aria-label="Card front">
      <span class="brand-front">VORENDA REALTY</span>
    </section>

    <section class="card card-back" aria-label="Card back">
      <div class="agent">
        <p class="agent-name">Helena Marsh</p>
        <p class="agent-role">Senior Property Consultant</p>
      </div>
      <div class="contact">
        <p class="contact-phone">0400 123 456</p>
        <p class="contact-web">www.vorendarealty.com.au</p>
      </div>
      <span class="brand-back">VORENDA REALTY</span>
      <address class="address" style="font-style:normal">
        7C, 48 Harbour Street<br>
        Eastwood, NSW 2100
      </address>
    </section>
  </main>
</body>
</html>
```